Weight loss surgery restaurant card

We need to create a card for patients who have undergone weight loss surgery to take to restaurants so they can request smaller meals. These patients have had surgery on their stomach so that they can only consume half to one cup of food at a time. So normal sized restaurant meals are way too big (and cost a lot). This card they can present to the restaurant to communicate the fact that they have had weight loss surgery and therefore request a smaller meal portion at reduced cost

Target Market(s)

Restaurants serving weight loss surgery patients

Industry/Entity Type

Health Care

Contact Information for Business Card

This will be a plastic card similar to business card size.

Requirements
Must have
• The front of the card should include the following text:
• The individual bearing this card has undergone weight loss surgery.
• This surgery restricts portion sizes to between half and one cup of food at a time.
• Please give consideration to allowing smaller portions of your regular meals to be ordered to reduce wastage and excess costs.
• Example: a half size portion priced at two thirds of usual cost.
• The back of the card will have spaces for the person to write certain information. These are the categories that can be filled in by hand:
• Name:
• Procedure performed:
• Date of procedure (month/year):
• Treating Clinic Name:
• Treating Clinic Signature:
• Somewhere down the bottom should be something along the lines of:
• supplied from bernardwhitlow.com.au
Nice to have
• A nice design with imagery/colours etc ... not just the text on a white background! Bright attractive colours preferred.
• I have uploaded my logo ... a roughly triangular image followed by my name etc. The triangular logo image could be used somewhere on the card and this logo can be interchangeable for other clinics who purchase the card.
• **Please note that I don't want my name to be included as part of the logo on the card ... just use the triangular image on the side of the logo without the following name**
• Also, the colouring of the card does not have to reflect my logo colours as I am anticipating interchanging this logo with other logos if other clinics choose to adopt the card. I am interested to see other, more generic, colour choices as well as my logo colours

```html
<!DOCTYPE html>
<html lang="en">
<head>
<meta charset="utf-8">
<title>Weight Loss Surgery Restaurant Card</title>
<link rel="stylesheet" href="https://fonts.googleapis.com/css2?family=Open+Sans:wght@300;400&family=Cinzel:wght@400&display=swap">
<style>
  :root {
    --backdrop: #2a2a2a;
    --card-light: #eeeeee;
    --teal: #16908a;
    --teal-rule: rgba(255,255,255,0.22);
    --ink: #333333;
    --ink-soft: #555555;
    --field-rule: #cfe0de;
    --white: #ffffff;
  }
  * { box-sizing: border-box; margin: 0; padding: 0; }
  html, body {
    width: 1200px; height: 1200px; overflow: hidden;
    background: var(--backdrop);
    font-family: "Open Sans", Arial, sans-serif;
  }
  .canvas { position: relative; width: 1200px; height: 1200px; }

  .card {
    position: absolute; top: 310px; height: 594px;
    box-shadow: 0 3px 8px rgba(0,0,0,0.5);
  }

  /* Details side */
  .card--details { left: 234px; width: 364px; background: var(--card-light); }
  .clinic-mark {
    position: absolute; top: 440px; left: 0; width: 100%;
    top: 148px; text-align: center;
    font-size: 26px; font-weight: 400; color: var(--teal);
    display: flex; align-items: center; justify-content: center; gap: 12px;
  }
  .clinic-mark__dot { width: 16px; height: 16px; border-radius: 50%; background: var(--teal); }
  .field {
    position: absolute; left: 32px; width: 292px;
    border-bottom: 1px solid var(--field-rule);
    font-size: 14.5px; color: var(--ink); letter-spacing: 0.2px;
  }

  /* Message side */
  .card--message { left: 627px; width: 369px; background: var(--teal); }
  .message-block {
    position: absolute; left: 0; width: 100%;
    text-align: center; color: var(--white);
    font-size: 15px; line-height: 22.5px; text-transform: uppercase;
  }
  .message-rule {
    position: absolute; left: 33px; width: 302px; height: 1px;
    background: var(--teal-rule);
  }
  .supplier {
    position: absolute; left: 0; bottom: 0; width: 100%; height: 89px;
    background: var(--card-light); text-align: center;
    padding-top: 25px;
  }
  .supplier__lead { font-size: 18px; font-weight: 300; color: var(--ink-soft); line-height: 22px; }
  .supplier__url {
    font-family: "Cinzel", Georgia, serif; font-size: 16px;
    color: var(--ink); letter-spacing: 1px; line-height: 22px;
  }
</style>
</head>
<body>
<main class="canvas">

  <section class="card card--details" aria-label="Card details side">
    <div class="clinic-mark"><span class="clinic-mark__dot"></span>Bernard Whitlow</div>
    <div class="field" style="top:292px;height:49px;">NAME:</div>
    <div class="field" style="top:348px;height:47px;">PROCEDURE PERFORMED:</div>
    <div class="field" style="top:404px;height:51px;">DATE OF PROCEDURE (MONTH/YEAR):</div>
    <div class="field" style="top:459px;height:50px;">TREATING CLINIC NAME:</div>
    <div class="field" style="top:515px;height:60px;">TREATING CLINIC SIGNATURE:</div>
  </section>

  <section class="card card--message" aria-label="Card message side">
    <p class="message-block" style="top:90px;">The individual bearing this card<br>has undergone weight loss surgery.</p>
    <div class="message-rule" style="top:142px;"></div>
    <p class="message-block" style="top:148px;">Around 500,000 of these procedures<br>are performed around the world<br>every year.</p>
    <div class="message-rule" style="top:219px;"></div>
    <p class="message-block" style="top:228px;">This surgery restricts portion<br>sizes to between half<br>and one cup of food at a time.</p>
    <div class="message-rule" style="top:306px;"></div>
    <p class="message-block" style="top:319px;">Please give consideration to allowing<br>smaller portions of your regular<br>meals to be ordered to reduce<br>wastage and excess costs.</p>
    <div class="message-rule" style="top:422px;"></div>
    <p class="message-block" style="top:431px;">Example: a half size portion<br>priced at two thirds of usual cost.</p>
    <div class="supplier">
      <p class="supplier__lead">Purchased through</p>
      <p class="supplier__url">WWW.BERNARDWHITLOW.COM.AU</p>
    </div>
  </section>

</main>
</body>
</html>
```